VEHICLE TUNING CHIP ONLINE SHOP

NEW ECOMMERCE SITE, SELLING TUNING CHIPS FOR VEHICLES -

performance and fuel efficiency tuning for cars, vans, jeeps, agri (tractors harvestors, trucks)

Must be user friendly layout - easy to understand, select product and purchase online.

Product: This is a computer chip which can be purchased by a customer, DIY installed to their vehicle using OEM plugs, for improved performance and fuel efficiency.

IDEAS:

1. KLV SYSTEMS

2. BOLTWERK.DE

3. MOXAGEARS.CO.UK

NEW BRAND - PRX (POWER REFLEX MODULE)
NEED A LOGO AND DESIGN IDEAS

Target Market(s)

AUTOMOTIVE SECTORS WORLDWIDE

Industry/Entity Type

Shop

Logo Text

PRX - CHIPTUNING

Number of Pages Required

1 page

Requirements
Must have
• nice layout - section for light vehicles ie. cars/vans . Section for agri vehicles ie. tractors
Nice to have
• KLV SYSTEMS website is very good. MGUK , BOLTWERK are also very good to get ideas from.

```html
<!DOCTYPE html>
<html lang="en">
<head>
<meta charset="utf-8">
<title>PRX Chiptuning – Light & Agri Vehicle Shop</title>
<link rel="stylesheet" href="https://fonts.googleapis.com/css2?family=Exo+2:ital,wght@0,600;0,800;1,800;1,900&family=Open+Sans:wght@400;600;700&display=swap">
<style>
:root{
  --ink:#111418;
  --teal:#173a44;
  --teal-deep:#0f2a32;
  --yellow:#f2c12e;
  --gold:#dca51c;
  --red:#e11d1d;
  --paper:#eef3f4;
  --grey:#9aa1a6;
  --mute:#b8bec2;
  --white:#ffffff;
  --head:"Exo 2",sans-serif;
  --body:"Open Sans",sans-serif;
}
*{box-sizing:border-box;margin:0;padding:0}
html,body{width:833px;height:1200px;overflow:hidden;background:var(--white);font-family:var(--body);color:var(--ink)}
.board{position:relative;width:833px;height:1200px}
.board-label{position:absolute;top:12px;font:600 10px/1 var(--body);letter-spacing:.2px}
.page{position:absolute;top:32px;width:395px;display:flex;flex-direction:column;background:var(--paper);box-shadow:0 0 3px rgba(0,0,0,.15)}
.page--light{left:6px}
.page--agri{left:431px}
.label--light{left:6px}.label--agri{left:431px}

/* hero */
.hero{position:relative;height:218px;overflow:hidden}
.hero-photo{position:absolute;inset:0}
.hero--light .hero-photo{background:linear-gradient(160deg,#e9e6e0 0%,#cdd1d4 35%,#8f979c 60%,#1f2a36 72%,#e6e4e0 100%)}
.hero--agri .hero-photo{background:linear-gradient(170deg,#4a4a4a 0%,#c9913b 30%,#e4a13e 45%,#2d5a24 62%,#2b2b1c 80%,#7a5a2a 100%)}
.hero-nav{position:absolute;top:12px;left:12px;right:12px;display:flex;align-items:center;justify-content:space-between}
.brand{display:flex;align-items:center;gap:4px;font:800 22px/1 var(--head);color:var(--ink)}
.hero--agri .brand{color:var(--white)}
.brand-mark{width:9px;height:9px;background:var(--yellow)}
.nav{display:flex;gap:7px;font:600 4.6px/1 var(--body);letter-spacing:.3px;color:#333}
.hero--agri .nav{color:#eee}
.hero-title{position:absolute;right:16px;top:46px;text-align:right;font:italic 800 14px/1.1 var(--head);color:#8b8f93;letter-spacing:.5px}
.hero--agri .hero-title{color:#fff}
.dots{position:absolute;bottom:12px;left:50%;transform:translateX(-50%);display:flex;gap:5px}
.dots i{width:2px;height:2px;border-radius:50%;background:#fff}
.tabs{display:flex;height:22px}
.tab{flex:1;display:flex;align-items:center;justify-content:center;font:600 6.4px/1 var(--body);color:#8a8f93;background:#5d6468}
.tab--active{background:var(--ink);color:#fff;position:relative}
.tab--active::after{content:"";position:absolute;bottom:5px;width:14px;height:1px;background:var(--yellow)}

/* features */
.features{height:90px;background:linear-gradient(180deg,var(--teal-deep),var(--teal));display:flex;padding:20px 0 0 70px;gap:34px}
.feature{width:60px;text-align:center}
.feature svg{width:26px;height:26px;display:block;margin:0 auto 6px}
.feature h3{font:800 7px/1 var(--head);color:var(--yellow);letter-spacing:.3px}
.feature p{font:700 4.8px/1.3 var(--body);color:#fff;letter-spacing:.3px}

/* promo bands */
.promo{position:relative;height:104px;overflow:hidden;background:linear-gradient(90deg,#f5f6f7,#c3c7ca)}
.promo--power{height:103px;margin-top:7px}
.promo-photo{position:absolute;top:0;bottom:0}
.promo-title{display:inline-block;background:var(--ink);color:var(--yellow);font:italic 900 12px/1 var(--head);padding:3px 10px 3px 44px;letter-spacing:.5px}
.promo-copy{font:italic 400 5.4px/1.25 var(--body);color:#444;margin-top:6px}
.big-stat{font:italic 900 22px/1 var(--head);color:var(--red)}
.stat-note{font:italic 800 7.4px/1 var(--head);color:var(--ink)}
.bullets{display:flex;gap:16px;font:italic 700 5px/1.3 var(--body);color:#222}
.bullets ul{list-style:none}
.device{position:absolute;background:linear-gradient(160deg,#55595d,#1d2023);border-radius:6px}

/* pilot */
.pilot{height:102px;margin-top:6px;position:relative;background:linear-gradient(90deg,#e8ecef,#d4d8dc)}
.pilot h2{position:absolute;left:33px;top:12px;font:italic 900 15px/1 var(--head)}
.pilot h4{position:absolute;left:62px;top:29px;font:italic 800 6.6px/1 var(--head);letter-spacing:.4px}
.pilot p{position:absolute;left:33px;top:42px;width:160px;font:600 5px/1.45 var(--body);color:#333}

/* products */
.products{padding:14px 0 0;text-align:center}
.section-title{font:italic 800 8px/1 var(--head);color:var(--red);letter-spacing:.5px}
.section-sub{font:400 4.2px/1 var(--body);color:#555;margin-top:3px}
.grid{display:grid;grid-template-columns:repeat(4,76px);gap:0 8px;justify-content:center;margin-top:10px;text-align:left}
.card-frame{position:relative;height:90px;background:#fff;border:1px solid #d6dadc}
.card-shot{position:absolute;left:14px;right:14px;top:14px;height:56px;border-radius:8px}
.card-shot--box{background:linear-gradient(160deg,#50555a,#16191c)}
.card-shot--pedal{left:26px;right:26px;background:linear-gradient(160deg,#d9dde0,#5d6368)}
.heart{position:absolute;left:5px;top:5px;width:8px;height:8px}
.price{position:absolute;left:5px;bottom:6px;background:var(--ink);color:#fff;font:700 3.8px/1 var(--body);padding:1.5px 4px}
.sale{position:absolute;left:18px;bottom:6px;background:var(--red);color:#fff;font:700 3.8px/1 var(--body);padding:1.5px 3px}
.shop{position:absolute;right:5px;bottom:6px;background:var(--yellow);color:#fff;font:700 3.6px/1 var(--body);padding:1.5px 5px}
.card-name{font:600 4.2px/1 var(--body);color:#333;margin-top:3px}
.card-meta{display:flex;justify-content:space-between;font:400 3.6px/1 var(--body);color:var(--mute);margin-top:2px}
.stars{color:var(--gold);letter-spacing:.5px}
.load{display:inline-block;margin-top:14px;border:1px solid #bbb;background:#fff;font:600 3.8px/1 var(--body);padding:2px 7px}

/* customers */
.customers{position:relative;background:linear-gradient(180deg,#e1ae23,#f0c33a 50%,#d9a11c);text-align:center;padding-top:14px}
.customers h2{font:italic 900 8.4px/1.05 var(--head);color:var(--ink);letter-spacing:.4px}
.customers p{font:400 4.2px/1.3 var(--body);color:#222;width:160px;margin:2px auto 0}
.faces{display:flex;justify-content:center;gap:9px;margin-top:10px;align-items:center}
.face{width:64px;height:54px;border:2px solid #fff}
.arrow{width:8px;height:12px}

/* footer */
.footer{padding:18px 30px 0 33px;position:relative;font-family:var(--body)}
.cols{display:flex;gap:0}
.col{width:56px}
.col h5{font:700 5px/1 var(--body);color:var(--red);margin-bottom:4px}
.col li{list-style:none;font:400 3.8px/1.5 var(--body);color:#333}
.service{position:absolute;right:32px;top:18px;text-align:right}
.service h5{font:700 5px/1 var(--body);color:var(--red)}
.service .phone{font:600 8.4px/1.2 var(--body);color:var(--red)}
.service b{display:block;font:700 4.4px/1.3 var(--body)}
.service small{display:block;font:400 3.6px/1.35 var(--body);color:#333}
.service .addr{color:var(--red);font-weight:700}
.pay h5{font:700 5px/1 var(--body);color:var(--red);margin:16px 0 6px}
.pay-row{display:flex;gap:10px;align-items:center}
.pay-name{font:700 8px/1 var(--body);color:#1d2b6b}
.news{position:absolute;right:62px;top:116px;width:110px;font:400 3.8px/1.4 var(--body);color:#333}
.news-form{display:flex;margin-top:6px}
.news-input{flex:1;height:10px;background:#fff;border:1px solid #ccc}
.news-btn{width:46px;height:10px;background:var(--yellow);font:700 4px/10px var(--body);text-align:center;color:var(--ink)}
.bar{background:var(--ink);display:flex;align-items:center;justify-content:space-between;padding:0 14px 0 33px}
.bar nav{display:flex;gap:10px;font:600 5px/1 var(--body);color:var(--yellow)}
.social{display:flex;gap:3px}
.social i{width:8px;height:8px;border-radius:50%;background:#fff}
</style>
</head>
<body>
<main class="board">
  <h1 class="board-label label--light">LIGHT VEHICLES SECTION</h1>
  <h1 class="board-label label--agri">AGRICULTURAL VEHICLES SECTION</h1>

  <!-- Light vehicles page -->
  <article class="page page--light" style="height:1160px">
    <header class="hero hero--light">
      <div class="hero-photo" role="img" aria-label="Dark blue SUV on a snowy mountain road at sunset"></div>
      <div class="hero-nav">
        <div class="brand"><span class="brand-mark"></span>PRX</div>
        <nav class="nav"><span>POWER CONTROL</span><span>PEDAL BOX</span><span>TECHNOLOGY</span><span>SERVICE</span><span>COMPANY</span><span>| MY ACCOUNT</span></nav>
      </div>
      <h2 class="hero-title">IMPROVED PERFORMANCE<br>AND EFFICIENCY</h2>
      <div class="dots"><i></i><i></i><i></i><i></i><i></i></div>
    </header>
    <div class="tabs"><div class="tab tab--active">LIGHT VEHICLES</div><div class="tab">AGRI VEHICLES</div></div>
    <section class="features">
      <div class="feature"><svg viewBox="0 0 26 26" fill="none" stroke="#fff" stroke-width="1.5"><circle cx="13" cy="13" r="10" stroke-dasharray="3 2"/><text x="13" y="16.5" font-size="9" font-weight="700" fill="#fff" stroke="none" text-anchor="middle" font-family="Open Sans">24</text></svg><h3>LOREM IPSUM</h3><p>DOLOR SIT AMET</p></div>
      <div class="feature"><svg viewBox="0 0 26 26" fill="none" stroke="#fff" stroke-width="1.6"><circle cx="10" cy="15" r="6"/><circle cx="10" cy="15" r="2"/><circle cx="19" cy="8" r="4"/><circle cx="19" cy="8" r="1.3"/></svg><h3>LOREM IPSUM</h3><p>DOLOR SIT AMET</p></div>
      <div class="feature"><svg viewBox="0 0 26 26" fill="none" stroke="#fff" stroke-width="1.6"><circle cx="13" cy="13" r="9"/><path d="M9 10h8v4l-4 4-4-4z" fill="#fff"/></svg><h3>LOREM IPSUM</h3><p>DOLOR SIT AMET</p></div>
    </section>
    <section class="promo">
      <div class="promo-photo" role="img" aria-label="Red convertible driving along a coastal town at dusk" style="left:221px;right:0;background:linear-gradient(160deg,#e7a26b,#7f90a3 45%,#a8262a 70%,#3d4249)"></div>
      <div class="device" role="img" aria-label="Pedal box controller unit" style="left:176px;top:2px;width:44px;height:94px"></div>
      <div style="padding-top:12px">
        <div class="promo-title">PEDAL BOX</div>
        <p class="promo-copy" style="margin-left:42px">Lorem ipsum dolor consectetur<br>sed do eiusmod tempor incididunt</p>
        <div style="display:flex;align-items:center;gap:4px;margin:2px 0 0 24px"><span class="big-stat">+10%</span><span class="stat-note">BETTER<br>&nbsp;&nbsp;&nbsp;ACCELERATION</span></div>
        <div class="bullets" style="margin-left:42px"><ul><li>• Excepteur sint</li><li>• Occaecat cupidatat</li><li>• Proident sunt</li></ul><ul><li>• Excepteur sint</li><li>• Occaecat cupidatat</li><li>• Proident sunt</li></ul></div>
      </div>
    </section>
    <section class="promo promo--power">
      <div class="promo-photo" role="img" aria-label="Silver off-road SUV on a dusty desert track" style="left:0;width:197px;background:linear-gradient(150deg,#c8d3dc,#b49c83 55%,#6a5a4b)"></div>
      <div class="device" role="img" aria-label="Power control tuning module" style="left:212px;top:12px;width:76px;height:80px;border-radius:10px"></div>
      <div style="position:absolute;left:290px;right:0;top:16px">
        <div class="promo-title" style="padding:2px 0 2px 8px;display:block;font-size:11.5px;line-height:1.2;margin-left:-10px">POWER<br>&nbsp;&nbsp;&nbsp;CONTROL</div>
        <p class="promo-copy" style="margin-top:4px;font-size:4.6px">Lorem ipsum dolor consectetur<br>sed do eiusmod tempor<br>incididunt</p>
        <div style="display:flex;align-items:center;gap:3px;margin-left:-14px"><span class="big-stat" style="font-size:14px">+30%</span><span class="stat-note" style="font-size:4.6px">MORE POWER<br>&nbsp;MORE TORQUE</span></div>
        <div class="bullets"><ul><li>• Excepteur sint</li><li>• Occaecat cupidatat</li></ul></div>
      </div>
    </section>
    <section class="pilot">
      <div role="img" aria-label="Rally driver standing beside his race car" style="position:absolute;right:0;top:0;bottom:0;width:200px;background:linear-gradient(90deg,rgba(212,216,220,0),#8b9197 40%,#2a3036 70%,#c9cdd1)"></div>
      <h2>LOREM IPSUM</h2>
      <h4>LOREM IPSUM DOLOR SIT AMET</h4>
      <p>Lorem ipsum dolor sit amet, consectetur adipiscing elit, sed do eiusmod tempor incididunt ut labore et dolore magna aliqua. Ut enim ad minim veniam, quis nostrud exercitation ullamco laboris nisi ut aliquip ex ea commodo consequat.</p>
    </section>
    <section class="products" style="height:180px">
      <h2 class="section-title">PRODUCTS BEST SELLING</h2>
      <p class="section-sub">Lorem ipsum dolor sit amet tellus</p>
      <div class="grid">
        <div class="card"><div class="card-frame"><svg class="heart" viewBox="0 0 10 10"><path d="M5 9 1 5a2.3 2.3 0 0 1 4-3 2.3 2.3 0 0 1 4 3z" fill="none" stroke="#e11d1d" stroke-width="1"/></svg><div class="card-shot card-shot--box" role="img" aria-label="Power control module"></div><span class="price">$100</span></div><p class="card-name">Product Name&nbsp; Here</p><p class="card-meta"><span>Lorem ipsum dolor</span></p></div>
        <div class="card"><div class="card-frame"><svg class="heart" viewBox="0 0 10 10"><path d="M5 9 1 5a2.3 2.3 0 0 1 4-3 2.3 2.3 0 0 1 4 3z" fill="none" stroke="#e11d1d" stroke-width="1"/></svg><div class="card-shot card-shot--pedal" role="img" aria-label="Pedal box unit"></div><span class="price">$100</span><span class="shop">Shop Now</span></div><p class="card-name">Product Name&nbsp; Here</p><p class="card-meta"><span>Lorem ipsum dolor</span><span class="stars">★★★★</span></p></div>
        <div class="card"><div class="card-frame"><svg class="heart" viewBox="0 0 10 10"><path d="M5 9 1 5a2.3 2.3 0 0 1 4-3 2.3 2.3 0 0 1 4 3z" fill="#e11d1d"/></svg><div class="card-shot card-shot--box" role="img" aria-label="Power control module"></div><span class="price">$100</span></div><p class="card-name">Product Name&nbsp; Here</p><p class="card-meta"><span>Lorem ipsum dolor</span><span class="stars">★★★★</span></p></div>
        <div class="card"><div class="card-frame"><svg class="heart" viewBox="0 0 10 10"><path d="M5 9 1 5a2.3 2.3 0 0 1 4-3 2.3 2.3 0 0 1 4 3z" fill="none" stroke="#e11d1d" stroke-width="1"/></svg><div class="card-shot card-shot--pedal" role="img" aria-label="Pedal box unit"></div><span class="price">$80</span><span class="sale">20%</span></div><p class="card-name">Product Name&nbsp; Here</p><p class="card-meta"><span>Lorem ipsum dolor</span></p></div>
      </div>
      <span class="load">LOAD MORE</span>
    </section>
    <section class="customers" style="height:132px">
      <h2>OUR SATISFIED<br>&nbsp;&nbsp;&nbsp;&nbsp;&nbsp;&nbsp;&nbsp;CUSTOMER</h2>
      <p>Lorem ipsum dolor sit amet, consectetur adipiscing elit, sed do eiusmod tempor incididunt ut labore et dolore magna aliqua</p>
      <div class="faces">
        <svg class="arrow" viewBox="0 0 8 12"><path d="M7 1 2 6l5 5" fill="none" stroke="#fff" stroke-width="2"/></svg>
        <div class="face" role="img" aria-label="Happy customer driving her car" style="background:linear-gradient(150deg,#cfd5da,#6f7780)"></div>
        <div class="face" role="img" aria-label="Tuned sports saloon on a race track" style="background:linear-gradient(150deg,#9fb0c2,#3e4a57)"></div>
        <div class="face" role="img" aria-label="Smiling customer at the wheel" style="background:linear-gradient(150deg,#d9c6a8,#7d6a52)"></div>
        <div class="face" role="img" aria-label="Customer in sunglasses behind the wheel" style="background:linear-gradient(150deg,#9cbad0,#4b5f70)"></div>
        <svg class="arrow" viewBox="0 0 8 12"><path d="M1 1l5 5-5 5" fill="none" stroke="#fff" stroke-width="2"/></svg>
      </div>
    </section>
    <footer class="footer" style="height:172px">
      <div class="cols">
        <div class="col"><h5>Products</h5><ul><li>Lorem ipsum</li><li>Tolor sit amet</li><li>Consectetur</li><li>Adipiscing elit</li><li>Sed do eiusmo</li><li>Tempor</li></ul></div>
        <div class="col"><h5>Technology</h5><ul><li>Lorem ipsum</li><li>Tolor sit amet</li><li>Consectetur</li><li>Adipiscing elit</li><li>Sed do eiusmo</li><li>Tempor</li></ul></div>
        <div class="col"><h5>Service</h5><ul><li>Lorem ipsum</li><li>Tolor sit amet</li><li>Consectetur</li><li>Adipiscing elit</li><li>Sed do eiusmo</li><li>Tempor</li></ul></div>
        <div class="col"><h5>Company</h5><ul><li>Lorem ipsum</li><li>Tolor sit amet</li><li>Consectetur</li><li>Adipiscing elit</li><li>Sed do eiusmo</li><li>Tempor</li></ul></div>
      </div>
      <div class="service"><h5>Service Number</h5><div class="phone">+12 555 010203</div><b>Business Hours</b><small>Mon - Fri 8:30 to 17:00 CET<br>Sat 8:30 to 13:30 CET</small><small class="addr">Address</small><small>Lorem ipsum dolor<br>Amet, consectetur adipiscing<br>Eiusmodt - 12345,<br>Incididunt</small></div>
      <div class="pay"><h5>Payment Methods</h5><div class="pay-row"><span class="pay-name" style="color:#c0392b">Kardo</span><span class="pay-name">Velta</span><span class="pay-name" style="color:#2a6fb5">Orbis</span><span class="pay-name" style="color:#444">Paxon</span></div></div>
      <div class="news">Subscribe to our Newsletter now!<br>Subscribe to our Chiptuning Newsletter and stay up-to-date with our news, great promotions and special offers.<div class="news-form"><span class="news-input"></span><span class="news-btn">Subscribe</span></div></div>
    </footer>
    <div class="bar" style="height:24px"><nav><span>Imprint</span><span>Terms of Trade</span><span>Data protection</span><span>Withdrawal</span></nav><div class="social"><i></i><i></i><i></i><i></i></div></div>
  </article>

  <!-- Agricultural vehicles page -->
  <article class="page page--agri" style="height:1162px">
    <header class="hero hero--agri">
      <div class="hero-photo" role="img" aria-label="Green tractor on a field at golden sunset"></div>
      <div class="hero-nav">
        <div class="brand"><span class="brand-mark"></span>PRX</div>
        <nav class="nav"><span>POWER CONTROL</span><span>PEDAL BOX</span><span>TECHNOLOGY</span><span>SERVICE</span><span>COMPANY</span><span>| MY ACCOUNT</span></nav>
      </div>
      <h2 class="hero-title">IMPROVED PERFORMANCE<br>AND EFFICIENCY</h2>
      <div class="dots"><i></i><i></i><i></i><i></i><i></i></div>
    </header>
    <div class="tabs"><div class="tab">LIGHT VEHICLES</div><div class="tab tab--active">AGRI VEHICLES</div></div>
    <section class="features">
      <div class="feature"><svg viewBox="0 0 26 26" fill="none" stroke="#fff" stroke-width="1.5"><circle cx="13" cy="13" r="10" stroke-dasharray="3 2"/><text x="13" y="16.5" font-size="9" font-weight="700" fill="#fff" stroke="none" text-anchor="middle" font-family="Open Sans">24</text></svg><h3>LOREM IPSUM</h3><p>DOLOR SIT AMET</p></div>
      <div class="feature"><svg viewBox="0 0 26 26" fill="none" stroke="#fff" stroke-width="1.6"><circle cx="10" cy="15" r="6"/><circle cx="10" cy="15" r="2"/><circle cx="19" cy="8" r="4"/><circle cx="19" cy="8" r="1.3"/></svg><h3>LOREM IPSUM</h3><p>DOLOR SIT AMET</p></div>
      <div class="feature"><svg viewBox="0 0 26 26" fill="none" stroke="#fff" stroke-width="1.6"><circle cx="13" cy="13" r="9"/><path d="M9 10h8v4l-4 4-4-4z" fill="#fff"/></svg><h3>LOREM IPSUM</h3><p>DOLOR SIT AMET</p></div>
    </section>
    <section class="promo">
      <div class="promo-photo" role="img" aria-label="Orange tractor driving between vineyard rows" style="left:221px;right:0;background:linear-gradient(160deg,#bfd3e3,#7ea25a 45%,#d2591f 65%,#3c4a2a)"></div>
      <div class="device" role="img" aria-label="Pedal box controller unit" style="left:176px;top:2px;width:44px;height:94px"></div>
      <div style="padding-top:12px">
        <div class="promo-title">PEDAL BOX</div>
        <p class="promo-copy" style="margin-left:42px">Lorem ipsum dolor consectetur<br>sed do eiusmod tempor incididunt</p>
        <div style="display:flex;align-items:center;gap:4px;margin:2px 0 0 24px"><span class="big-stat">+10%</span><span class="stat-note">BETTER<br>&nbsp;&nbsp;&nbsp;ACCELERATION</span></div>
        <div class="bullets" style="margin-left:42px"><ul><li>• Excepteur sint</li><li>• Occaecat cupidatat</li><li>• Proident sunt</li></ul><ul><li>• Excepteur sint</li><li>• Occaecat cupidatat</li><li>• Proident sunt</li></ul></div>
      </div>
    </section>
    <section class="promo promo--power">
      <div class="promo-photo" role="img" aria-label="Blue tractor pulling a baler across a wheat field" style="left:0;width:197px;background:linear-gradient(160deg,#dfe6ec,#2f5aa8 45%,#c9a85e 70%,#7c6a3a)"></div>
      <div class="device" role="img" aria-label="Power control tuning module" style="left:212px;top:12px;width:76px;height:80px;border-radius:10px"></div>
      <div style="position:absolute;left:290px;right:0;top:16px">
        <div class="promo-title" style="padding:2px 0 2px 8px;display:block;font-size:11.5px;line-height:1.2;margin-left:-10px">POWER<br>&nbsp;&nbsp;&nbsp;CONTROL</div>
        <p class="promo-copy" style="margin-top:4px;font-size:4.6px">Lorem ipsum dolor consectetur<br>sed do eiusmod tempor<br>incididunt</p>
        <div style="display:flex;align-items:center;gap:3px;margin-left:-14px"><span class="big-stat" style="font-size:14px">+30%</span><span class="stat-note" style="font-size:4.6px">MORE POWER<br>&nbsp;MORE TORQUE</span></div>
        <div class="bullets"><ul><li>• Excepteur sint</li><li>• Occaecat cupidatat</li></ul></div>
      </div>
    </section>
    <section class="products" style="height:286px">
      <h2 class="section-title">PRODUCTS BEST SELLING</h2>
      <p class="section-sub">Lorem ipsum dolor sit amet tellus</p>
      <div class="grid" style="row-gap:12px">
        <div class="card"><div class="card-frame"><svg class="heart" viewBox="0 0 10 10"><path d="M5 9 1 5a2.3 2.3 0 0 1 4-3 2.3 2.3 0 0 1 4 3z" fill="none" stroke="#e11d1d" stroke-width="1"/></svg><div class="card-shot card-shot--box" role="img" aria-label="Power control module"></div><span class="price">$100</span></div><p class="card-name">Product Name&nbsp; Here</p><p class="card-meta"><span>Lorem ipsum dolor</span></p></div>
        <div class="card"><div class="card-frame"><svg class="heart" viewBox="0 0 10 10"><path d="M5 9 1 5a2.3 2.3 0 0 1 4-3 2.3 2.3 0 0 1 4 3z" fill="none" stroke="#e11d1d" stroke-width="1"/></svg><div class="card-shot card-shot--pedal" role="img" aria-label="Pedal box unit"></div><span class="price">$100</span><span class="shop">Shop Now</span></div><p class="card-name">Product Name&nbsp; Here</p><p class="card-meta"><span>Lorem ipsum dolor</span><span class="stars">★★★★</span></p></div>
        <div class="card"><div class="card-frame"><svg class="heart" viewBox="0 0 10 10"><path d="M5 9 1 5a2.3 2.3 0 0 1 4-3 2.3 2.3 0 0 1 4 3z" fill="#e11d1d"/></svg><div class="card-shot card-shot--box" role="img" aria-label="Power control module"></div><span class="price">$100</span></div><p class="card-name">Product Name&nbsp; Here</p><p class="card-meta"><span>Lorem ipsum dolor</span><span class="stars">★★★★</span></p></div>
        <div class="card"><div class="card-frame"><svg class="heart" viewBox="0 0 10 10"><path d="M5 9 1 5a2.3 2.3 0 0 1 4-3 2.3 2.3 0 0 1 4 3z" fill="none" stroke="#e11d1d" stroke-width="1"/></svg><div class="card-shot card-shot--pedal" role="img" aria-label="Pedal box unit"></div><span class="price">$80</span><span class="sale">20%</span></div><p class="card-name">Product Name&nbsp; Here</p><p class="card-meta"><span>Lorem ipsum dolor</span></p></div>
        <div class="card"><div class="card-frame"><svg class="heart" viewBox="0 0 10 10"><path d="M5 9 1 5a2.3 2.3 0 0 1 4-3 2.3 2.3 0 0 1 4 3z" fill="none" stroke="#e11d1d" stroke-width="1"/></svg><div class="card-shot card-shot--box" role="img" aria-label="Power control module"></div><span class="price">$100</span></div><p class="card-name">Product Name&nbsp; Here</p><p class="card-meta"><span>Lorem ipsum dolor</span></p></div>
        <div class="card"><div class="card-frame"><svg class="heart" viewBox="0 0 10 10"><path d="M5 9 1 5a2.3 2.3 0 0 1 4-3 2.3 2.3 0 0 1 4 3z" fill="none" stroke="#e11d1d" stroke-width="1"/></svg><div class="card-shot card-shot--pedal" role="img" aria-label="Pedal box unit"></div><span class="price">$100</span><span class="shop">Shop Now</span></div><p class="card-name">Product Name&nbsp; Here</p><p class="card-meta"><span>Lorem ipsum dolor</span><span class="stars">★★★★</span></p></div>
        <div class="card"><div class="card-frame"><svg class="heart" viewBox="0 0 10 10"><path d="M5 9 1 5a2.3 2.3 0 0 1 4-3 2.3 2.3 0 0 1 4 3z" fill="#e11d1d"/></svg><div class="card-shot card-shot--box" role="img" aria-label="Power control module"></div><span class="price">$100</span></div><p class="card-name">Product Name&nbsp; Here</p><p class="card-meta"><span>Lorem ipsum dolor</span><span class="stars">★★★★</span></p></div>
        <div class="card"><div class="card-frame"><svg class="heart" viewBox="0 0 10 10"><path d="M5 9 1 5a2.3 2.3 0 0 1 4-3 2.3 2.3 0 0 1 4 3z" fill="none" stroke="#e11d1d" stroke-width="1"/></svg><div class="card-shot card-shot--pedal" role="img" aria-label="Pedal box unit"></div><span class="price">$80</span><span class="sale">20%</span></div><p class="card-name">Product Name&nbsp; Here</p><p class="card-meta"><span>Lorem ipsum dolor</span></p></div>
      </div>
      <span class="load">LOAD MORE</span>
    </section>
    <section class="customers" style="height:136px">
      <h2>OUR SATISFIED<br>&nbsp;&nbsp;&nbsp;&nbsp;&nbsp;&nbsp;&nbsp;CUSTOMER</h2>
      <p>Lorem ipsum dolor sit amet, consectetur adipiscing elit, sed do eiusmod tempor incididunt ut labore et dolore magna aliqua</p>
      <div class="faces">
        <svg class="arrow" viewBox="0 0 8 12"><path d="M7 1 2 6l5 5" fill="none" stroke="#fff" stroke-width="2"/></svg>
        <div class="face" role="img" aria-label="Farmer on a small tractor" style="background:linear-gradient(150deg,#b9c7d3,#5e6a74)"></div>
        <div class="face" role="img" aria-label="Blue tractors parked in a yard" style="background:linear-gradient(150deg,#a8bfd6,#2c4e8a)"></div>
        <div class="face" role="img" aria-label="Farmer in a utility vehicle" style="background:linear-gradient(150deg,#8a9a6a,#3a4030)"></div>
        <div class="face" role="img" aria-label="Driver in a green tractor cab" style="background:linear-gradient(150deg,#a6d46a,#3f6a2c)"></div>
        <svg class="arrow" viewBox="0 0 8 12"><path d="M1 1l5 5-5 5" fill="none" stroke="#fff" stroke-width="2"/></svg>
      </div>
    </section>
    <footer class="footer" style="height:170px">
      <div class="cols">
        <div class="col"><h5>Products</h5><ul><li>Lorem ipsum</li><li>Tolor sit amet</li><li>Consectetur</li><li>Adipiscing elit</li><li>Sed do eiusmo</li><li>Tempor</li></ul></div>
        <div class="col"><h5>Technology</h5><ul><li>Lorem ipsum</li><li>Tolor sit amet</li><li>Consectetur</li><li>Adipiscing elit</li><li>Sed do eiusmo</li><li>Tempor</li></ul></div>
        <div class="col"><h5>Service</h5><ul><li>Lorem ipsum</li><li>Tolor sit amet</li><li>Consectetur</li><li>Adipiscing elit</li><li>Sed do eiusmo</li><li>Tempor</li></ul></div>
        <div class="col"><h5>Company</h5><ul><li>Lorem ipsum</li><li>Tolor sit amet</li><li>Consectetur</li><li>Adipiscing elit</li><li>Sed do eiusmo</li><li>Tempor</li></ul></div>
      </div>
      <div class="service"><h5>Service Number</h5><div class="phone">+12 555 010203</div><b>Business Hours</b><small>Mon - Fri 8:30 to 17:00 CET<br>Sat 8:30 to 13:30 CET</small><small class="addr">Address</small><small>Lorem ipsum dolor<br>Amet, consectetur adipiscing<br>Eiusmodt - 12345,<br>Incididunt</small></div>
      <div class="pay"><h5>Payment Methods</h5><div class="pay-row"><span class="pay-name" style="color:#c0392b">Kardo</span><span class="pay-name">Velta</span><span class="pay-name" style="color:#2a6fb5">Orbis</span><span class="pay-name" style="color:#444">Paxon</span></div></div>
      <div class="news">Subscribe to our Newsletter now!<br>Subscribe to our Chiptuning Newsletter and stay up-to-date with our news, great promotions and special offers.<div class="news-form"><span class="news-input"></span><span class="news-btn">Subscribe</span></div></div>
    </footer>
    <div class="bar" style="height:26px"><nav><span>Imprint</span><span>Terms of Trade</span><span>Data protection</span><span>Withdrawal</span></nav><div class="social"><i></i><i></i><i></i><i></i></div></div>
  </article>
</main>
</body>
</html>
```